Verpackungsdesign für Outdoor-Produkt
Lurvo suchte ein neues Design in der Kategorie Verpackungen und hat ein Projekt auf gestaltwerk-portal.de gestartet.
Zielgruppe
Wir verkaufen einzigartige Outdoor Produkte. Der Feuerstahl richtet sich an alle, die gerne in der Natur übernachten und beim Feuermachen noch selbst Hand anlegen wollen. Die Zielgruppe interessiert sich für Bushcraft & Survival, ist größtenteils Männlich und zwischen 30-40 Jahre alt.
Aufgabenstellung
Auf die obere Seite der Verpackung sollen das Logo und der Produktname platziert werden. Das Produkt gibt es in zwei Varianten, deshalb auch zwei verschiedene Namen.
Auf der vorderen Seite sollen die Features hervorgehoben werden. Dafür zum Beispiel ein passendes Icon finden und die Eigenschaft dazu (Beispiel: 'Flammen'-Icon, Bis zu 20.000 Zündungen garantiert).
An den Seiten links und rechts reicht das Logo.
Auf die hintere Seite kommt das Impressum.
Die Verpackung besteht aus braunem Karton.

```html
<!DOCTYPE html>
<html lang="de">
<head>
<meta charset="utf-8">
<title>Feuerstahl Basic – Faltschachtel</title>
<link rel="stylesheet" href="https://fonts.googleapis.com/css2?family=Roboto+Slab:wght@300;400;700;800&display=swap">
<style>
  :root {
    --paper: #ffffff;
    --ink: #111111;
    --cut: #2a2a2a;
    --fold: #e8352d;
  }
  html, body {
    margin: 0;
    padding: 0;
    width: 873px;
    height: 1200px;
    overflow: hidden;
    background: var(--paper);
  }
  .dieline-sheet {
    position: absolute;
    left: 0;
    top: 341px;
    width: 873px;
    height: 518px;
  }
  .cut-line { fill: none; stroke: var(--cut); stroke-width: 1.4; }
  .fold-line { fill: none; stroke: var(--fold); stroke-width: 1.2; }
  .icon { fill: none; stroke: var(--ink); stroke-width: 2.4; stroke-linecap: round; stroke-linejoin: round; }
  .slab { font-family: "Roboto Slab", serif; fill: var(--ink); }
  .product-name { font-weight: 800; font-size: 25px; }
  .product-variant { font-weight: 300; font-size: 23px; }
  .brand-name { font-weight: 700; font-size: 40px; letter-spacing: 2px; }
  .imprint { font-size: 12px; font-weight: 400; }
  .imprint-strong { font-size: 12px; font-weight: 700; }
  .feature-title { font-size: 13px; font-weight: 400; }
  .feature-text { font-size: 10px; font-weight: 400; }
</style>
</head>
<body>
<svg class="dieline-sheet" viewBox="0 100 1600 950" xmlns="http://www.w3.org/2000/svg">
  <!-- Deckelklappe -->
  <g class="lid-flap">
    <path class="cut-line" d="M403 147 H1198"/>
    <path class="cut-line" d="M403 152 C350 155 303 190 303 215 V265 C303 273 308 278 316 278 H390 L403 290"/>
    <path class="cut-line" d="M1198 152 C1251 155 1297 190 1297 215 V265 C1297 273 1292 278 1284 278 H1210 L1198 290"/>
    <path class="fold-line" d="M403 147 V290 M1198 147 V290 M403 290 H1198"/>
  </g>

  <!-- Oberseite -->
  <g class="top-panel">
    <path class="cut-line" d="M403 290 L395 298 V497 L407 505 M1198 290 L1206 298 V497 L1193 505"/>
    <path class="fold-line" d="M407 505 H1193"/>
    <g transform="translate(800 400)">
      <rect x="-16" y="-66" width="32" height="32" fill="none" stroke="var(--ink)" stroke-width="2.4"/>
      <text class="slab brand-name" x="0" y="20" text-anchor="middle">WALDFUNKE</text>
    </g>
    <text class="slab product-name" x="1172" y="336" text-anchor="end">FEUERSTAHL</text>
    <text class="slab product-variant" x="1172" y="362" text-anchor="end">BASIC</text>
  </g>

  <!-- Zwischenseite mit Seitenlaschen -->
  <g class="inner-panel">
    <path class="cut-line" d="M407 505 L397 515 H307 V637 H397 C405 637 407 642 407 650"/>
    <path class="cut-line" d="M1193 505 L1203 515 H1293 V637 H1203 C1195 637 1193 642 1193 650"/>
    <path class="fold-line" d="M407 505 V650 M1193 505 V650 M397 650 H1203"/>
  </g>

  <!-- Rückseite mit Seitenteilen -->
  <g class="back-panel">
    <path class="cut-line" d="M397 650 H257 L236 656 H104 V720 H85 V780 H104 V851 H236 L257 857 H413"/>
    <path class="cut-line" d="M1203 650 H1343 L1364 656 H1496 V720 H1515 V780 H1496 V851 H1364 L1343 857 H1187"/>
    <path class="cut-line" d="M397 722 H417 V784 H397 M1203 722 H1183 V784 H1203"/>
    <path class="fold-line" d="M397 650 V857 M1203 650 V857 M257 650 V857 M236 656 V851 M1343 650 V857 M1364 656 V851"/>
    <text class="slab imprint-strong" x="800" y="727" text-anchor="middle">Waldfunke</text>
    <text class="slab imprint" x="800" y="755" text-anchor="middle">Am Kiefernhang 7 · 21079 Hamburg · Deutschland</text>
    <text class="slab imprint" x="800" y="783" text-anchor="middle">kundenservice@waldfunke.de</text>
    <text class="slab imprint-strong" x="800" y="797" text-anchor="middle">www.waldfunke.de</text>
  </g>

  <!-- Vorderseite mit Features -->
  <g class="front-panel">
    <path class="cut-line" d="M413 857 L404 869 H314 V991 H404 L413 997 H1187 L1196 991 H1286 V869 H1196 L1187 857"/>
    <path class="fold-line" d="M413 857 V997 M1187 857 V997 M397 857 H1203"/>

    <g class="feature feature-sparks">
      <path class="icon" d="M546 878 C552 888 557 893 556 899 C555 906 550 909 546 909 C541 909 536 905 536 899 C536 893 541 890 541 886 C544 889 545 891 546 893 C548 889 548 884 546 878 Z"/>
      <text class="slab feature-title" x="546" y="929" text-anchor="middle">3000 °C HEIßE</text>
      <text class="slab feature-title" x="546" y="943" text-anchor="middle">FUNKEN</text>
      <text class="slab feature-text" x="546" y="960" text-anchor="middle">Mehr als 20.000</text>
      <text class="slab feature-text" x="546" y="972" text-anchor="middle">Zündungen garantiert</text>
    </g>

    <g class="feature feature-rod">
      <path class="icon" d="M679 886 L720 898 L718 904 L677 892 Z"/>
      <text class="slab feature-title" x="697" y="929" text-anchor="middle">XXL</text>
      <text class="slab feature-title" x="697" y="943" text-anchor="middle">ZÜNDSTAB</text>
      <text class="slab feature-text" x="697" y="960" text-anchor="middle">12,7 cm lang,</text>
      <text class="slab feature-text" x="697" y="972" text-anchor="middle">1,27 cm Durchmesser</text>
    </g>

    <g class="feature feature-striker">
      <path class="icon" d="M851 902 L878 884 C884 881 888 886 884 890 L862 905 Z M851 902 L849 906 L862 905"/>
      <circle cx="879" cy="888" r="1.5" fill="var(--ink)"/>
      <text class="slab feature-title" x="867" y="929" text-anchor="middle">SURVIVAL STRIKER</text>
      <text class="slab feature-text" x="868" y="948" text-anchor="middle">Hochwertiger 8Cr13MoV Stahl,</text>
      <text class="slab feature-text" x="868" y="960" text-anchor="middle">läßt sich im Notfall sogar zu</text>
      <text class="slab feature-text" x="868" y="972" text-anchor="middle">Mini Messer schärfen</text>
    </g>

    <g class="feature feature-weather">
      <path class="icon" d="M994 890 H1020 C1026 890 1026 883 1021 883 M1000 896 H1035 M994 902 H1024 C1030 902 1030 909 1025 909"/>
      <path class="icon" d="M1054 890 C1050 897 1048 900 1048 903 C1048 907 1051 909 1054 909 C1057 909 1060 907 1060 903 C1060 900 1058 897 1054 890 Z"/>
      <path class="icon" d="M1068 882 C1065 887 1064 889 1064 891 C1064 894 1066 895 1068 895 C1070 895 1072 894 1072 891 C1072 889 1071 887 1068 882 Z"/>
      <path class="icon" d="M1096 882 V908 M1085 888 L1107 902 M1107 888 L1085 902 M1092 883 L1096 887 L1100 883 M1092 907 L1096 903 L1100 907"/>
      <text class="slab feature-title" x="1050" y="929" text-anchor="middle">WIND-/WASSER-/</text>
      <text class="slab feature-title" x="1050" y="943" text-anchor="middle">KÄLTE-RESIST</text>
      <text class="slab feature-text" x="1050" y="960" text-anchor="middle">Schutz bei</text>
      <text class="slab feature-text" x="1050" y="972" text-anchor="middle">allen Witterungen</text>
    </g>
  </g>
</svg>
</body>
</html>
```